Crestline Supply Software Design

I would like a construction focused flyer design (if possible, inline with the current design esthetic from my website www.crsupsw.com), 1 standard US page (8.5x11"), front and back, full color glossy. I want a design I can use for multiple software partners, so I want the ability to edit the template that is created. This can be full page or folded- whatever you think is best.Attached are my logos, and a current flyer. I want to use the logo and the color scheme- feel free to make the logo colors even brighter. Everything else can be changed! Any additional graphics should be software or construction focused.

Target Market(s)

Electrical, Mechanical and Plumbing Construction Companies, specifically their accounting, IT, purchasing staff.

Font styles to use
Sans Serif

Colors
6b449b
9ccb3b

Requirements
Must have
• Lots of construction oriented graphics. Discreet boxes for text that can be changed in using photoshop or Illustrator products CS6 or earlier.
• Designs should be:
• - B2B focused
• - merge technology and construction
• - Show how technology can save time
• - Automation is a good thing
Should not have
• Be saved in a format that can not be used by CS6 or earlier.

```html
<!DOCTYPE html>
<html lang="en">
<head>
<meta charset="utf-8">
<title>Crestline Supply Software – Flyer Front and Back</title>
<link rel="stylesheet" href="https://fonts.googleapis.com/css2?family=Source+Sans+3:wght@400;600;700&display=swap">
<style>
:root{
  --purple:#6b449b;
  --purple-deep:#5a3789;
  --green:#9ccb3b;
  --ink:#2b2b2d;
  --text:#555;
  --panel:#3b3b3e;
  --panel-dark:#28282a;
  --black:#1c1c1d;
  --stage:#dcdad6;
  --white:#fff;
}
*{box-sizing:border-box;margin:0;padding:0}
html,body{width:1200px;height:805px;overflow:hidden}
body{background:var(--stage);font-family:"Source Sans 3",Arial,sans-serif;color:var(--ink);position:relative}
.flyer{position:absolute;top:54px;height:692px;background:var(--white);overflow:hidden;box-shadow:0 2px 10px rgba(0,0,0,.18)}
.flyer--front{left:45px;width:534px}
.flyer--back{left:632px;width:536px}
.abs{position:absolute}

/* brand */
.brand{position:absolute;display:flex;align-items:center;gap:10px}
.brand__mark{width:46px;height:46px;border-radius:50%;background:var(--green);flex:none}
.brand__name{font-weight:600;font-size:18.5px;line-height:23px;letter-spacing:.6px;text-transform:uppercase;color:var(--ink)}

/* photo placeholders */
.photo{position:absolute}
.photo--desk{left:0;top:0;width:534px;height:262px;
  background:linear-gradient(160deg,#9fb4c6 0%,#7d8e9c 35%,#a57a52 70%,#8a5f3a 100%);
  clip-path:polygon(0 0,100% 0,100% 100%,66% 100%,56% 224px,0 224px)}
.photo--crew{left:0;top:64px;width:536px;height:252px;
  background:linear-gradient(120deg,#9aa36a 0%,#c7cf8a 30%,#d7dbe0 60%,#b89a8a 100%);
  clip-path:polygon(0 50px,312px 50px,360px 0,100% 0,100% 100%,0 100%)}
.crew-edge{position:absolute;left:0;top:60px;width:536px;height:60px}
.badge{position:absolute;width:92px;height:92px;border-radius:50%;border:5px solid var(--purple);box-shadow:0 0 0 3px #bdbdbd, 0 6px 8px rgba(0,0,0,.25)}
.badge--site{left:323px;top:212px;background:linear-gradient(150deg,#8fb8d8,#c9a24a 70%,#6a6a60)}
.badge--loader{left:429px;top:212px;background:linear-gradient(150deg,#d9a24c,#8b6a43 60%,#4b4034)}

/* front copy */
.headline{left:18px;top:336px;width:500px;font-size:15.2px;font-weight:700;color:var(--purple);text-transform:uppercase;letter-spacing:0;white-space:nowrap}
.lineup{left:20px;top:364px;font-size:10px;font-weight:700;text-transform:uppercase;color:var(--ink)}
.intro{left:20px;top:380px;width:498px;font-size:8.6px;line-height:10.8px;color:var(--text)}

/* tabs */
.tab{position:absolute;left:0;background:var(--purple);color:var(--white);border-radius:0 14px 14px 0;display:flex;align-items:center}
.tab--products{top:431px;width:266px;height:30px;padding-left:18px;font-size:15px;font-weight:600;text-transform:uppercase}
.tab--why{top:303px;width:294px;height:30px;padding-left:19px;font-size:15px;font-weight:600}

/* product band */
.band{position:absolute;left:0;top:447px;width:100%;height:150px;border-top:3px solid var(--purple);
  background:linear-gradient(180deg,var(--panel) 0%,var(--panel-dark) 100%)}
.product{position:absolute;text-align:center;color:var(--white)}
.product__icon{display:block;margin:0 auto;border:3px solid var(--white);border-radius:50%;background:#46464a}
.product__title{font-weight:700;text-transform:uppercase;white-space:nowrap}
.product__desc{font-size:7px;line-height:8.2px;color:#e4e4e4}
.product__list{list-style:none;text-align:left;font-size:7px;line-height:9.2px;color:#e4e4e4;white-space:nowrap}
.product__list li::before{content:"• "}
.flyer--front .product{top:14px;width:118px}
.flyer--front .product__icon{width:50px;height:50px}
.flyer--front .product__title{font-size:10px;margin-top:13px;margin-bottom:2px}
.flyer--back .product{top:7px;width:172px}
.flyer--back .product__icon{width:58px;height:58px}
.flyer--back .product__title{font-size:11.5px;margin-top:11px;margin-bottom:8px;text-align:center}

/* body copy back */
.summary{left:25px;top:343px;width:487px;font-size:12.2px;line-height:16.6px;color:var(--text);text-align:justify}

/* social dots */
.social{position:absolute;top:27px;width:16px;height:16px;border-radius:50%;border:1px solid #9a9a9a}

/* call to action */
.cta{position:absolute;left:0;top:597px;width:100%;height:53px;text-align:center}
.cta__line{font-size:14.6px;font-weight:600;text-transform:uppercase;letter-spacing:.2px;color:var(--ink);padding-top:12px}
.cta__pill{position:absolute;left:50%;transform:translateX(-50%);top:39px;z-index:2;height:26px;padding:0 14px;border-radius:9px;background:var(--purple);color:var(--white);font-size:12px;font-weight:600;display:flex;align-items:center;gap:6px;white-space:nowrap}
.cta__pill svg{width:11px;height:11px}
.footer{position:absolute;left:0;bottom:0;width:100%;height:42px;background:linear-gradient(90deg,var(--black),#3a3a3c 50%,var(--black));color:var(--white);font-size:12.5px;font-weight:600;letter-spacing:1.6px;text-align:center;padding-top:18px}
</style>
</head>
<body>

<!-- FRONT -->
<section class="flyer flyer--front">
  <div class="photo photo--desk" role="img" aria-label="Construction desk scene with tablet, yellow hard hat, blueprints and smartphone in front of a building site"></div>
  <div class="badge badge--site" role="img" aria-label="Round photo of a construction worker at a site"></div>
  <div class="badge badge--loader" role="img" aria-label="Round photo of a wheel loader moving soil"></div>

  <div class="brand" style="left:18px;top:253px">
    <span class="brand__mark"></span>
    <span class="brand__name">Crestline<br>Supply<br>Software</span>
  </div>

  <h1 class="abs headline">Finally! Affordable software to produce professional PO's!</h1>
  <p class="abs lineup">Rapid Purchase - Rapid Order - Rapid Invoice</p>
  <p class="abs intro">With over 25 years in the construction industry, we understand the frustration of inefficient procurement processes, the financial pains and ramifications of setbacks, and the need for consistently flawless execution of purchasing tasks. With an industry average of less than 6% profit per project, we know what's on the line.</p>

  <div class="band">
    <div class="product" style="left:18px">
      <svg class="product__icon" viewBox="0 0 50 50"><text x="25" y="34" text-anchor="middle" font-size="28" font-weight="700" fill="#6b449b" font-family="Source Sans 3,Arial,sans-serif">$</text></svg>
      <p class="product__title">Rapid Purchase</p>
      <p class="product__desc">Rapid Purchase is a comprehensive, easy-to-use software package for material management.</p>
    </div>
    <div class="product" style="left:145px">
      <svg class="product__icon" viewBox="0 0 50 50"><path d="M13 26 L37 15 L30 37 L25 29 Z" fill="#6b449b"/><path d="M25 29 L37 15" stroke="#46464a" stroke-width="1.5"/></svg>
      <p class="product__title">Rapid Order</p>
      <p class="product__desc">Rapid Order Confirmation uses the latest technology to harness all of the information your vendor has about your order and then makes that information available to you.</p>
    </div>
    <div class="product" style="left:286px">
      <svg class="product__icon" viewBox="0 0 50 50"><path d="M12 32 A13 13 0 0 1 38 32 Z" fill="#6b449b"/><path d="M25 32 L31 22" stroke="#fff" stroke-width="2.5" stroke-linecap="round"/><circle cx="25" cy="32" r="2.5" fill="#fff"/></svg>
      <p class="product__title">Rapid Invoice</p>
      <p class="product__desc">Tired of trying to match invoice items to order items? Rapid Invoice builds on what Rapid Order Confirmation started.</p>
    </div>
    <div class="product" style="left:408px">
      <svg class="product__icon" viewBox="0 0 50 50"><path d="M15 15 L35 35 M35 15 L15 35" stroke="#6b449b" stroke-width="5" stroke-linecap="round"/></svg>
      <p class="product__title">Gear Tracker</p>
      <p class="product__desc">Gear Tracker follows the Rapid Purchase design, which incorporates ease of use with an intuitive, user friendly interface.</p>
    </div>
  </div>
  <div class="tab tab--products">Our Products</div>

  <div class="cta">
    <p class="cta__line">Let us show you how you can take your PO's to the next level</p>
    <div class="cta__pill">Call Crestline Supply on
      <svg viewBox="0 0 12 12"><circle cx="6" cy="6" r="5.2" fill="none" stroke="#fff" stroke-width="1"/><path d="M4 3.5 L5 5 L4.6 5.6 Q5.3 7 6.4 7.4 L7 7 L8.5 8 L7.8 8.9 Q5 8.6 3.2 4.3 Z" fill="#fff"/></svg>
      (800) 555-0142 &nbsp;for an obligation free quote</div>
  </div>
  <div class="footer">www.crsupsw.com</div>
</section>

<!-- BACK -->
<section class="flyer flyer--back">
  <div class="brand" style="left:18px;top:36px">
    <span class="brand__mark"></span>
    <span class="brand__name">Crestline<br>Supply<br>Software</span>
  </div>
  <span class="social" style="left:418px"></span>
  <span class="social" style="left:445px"></span>
  <span class="social" style="left:472px"></span>
  <span class="social" style="left:499px"></span>

  <div class="photo photo--crew" role="img" aria-label="Two construction engineers in hard hats and safety vests reviewing plans on a building site"></div>
  <svg class="crew-edge" viewBox="0 0 536 60" aria-hidden="true"><polyline points="0,56 312,56 360,4 536,4" fill="none" stroke="#6b449b" stroke-width="3"/></svg>

  <div class="tab tab--why">Why frustrate when you can automate!</div>
  <p class="abs summary">CRESTLINE SUPPLY SOFTWARE offers three levels of automation and procurement expertise across the acquisition life cycle. CRESTLINE SUPPLY offers a full-fledged items based materials system, an automated purchase order acknowledgement system, and an invoice matching suite to take the guess work out of vendor payments- and all of this works with your accounting system.</p>

  <div class="band">
    <div class="product" style="left:14px">
      <svg class="product__icon" viewBox="0 0 58 58"><rect x="19" y="15" width="20" height="7" rx="1" fill="#6b449b"/><rect x="19" y="24" width="20" height="7" rx="1" fill="#6b449b"/><rect x="19" y="33" width="20" height="7" rx="1" fill="#6b449b"/><path d="M29 40 V45 M21 45 H37" stroke="#6b449b" stroke-width="2"/></svg>
      <p class="product__title">Rapid Purchase</p>
      <ul class="product__list"><li>Swiftly create professional-looking POs</li><li>Track orders to jobsites</li><li>Review cumulated jobsite material usage</li><li>Link to your accounting system</li></ul>
    </div>
    <div class="product" style="left:183px">
      <svg class="product__icon" viewBox="0 0 58 58"><rect x="18" y="15" width="22" height="28" rx="2" fill="#6b449b"/><rect x="24" y="12" width="10" height="6" rx="1.5" fill="#fff"/><path d="M23 30 L27 34 L35 25" stroke="#fff" stroke-width="2.5" fill="none" stroke-linecap="round"/></svg>
      <p class="product__title">Rapid Order Confirmation</p>
      <ul class="product__list"><li>Create POs of any size in less than a minute</li><li>Quickly get material orders to your vendors</li><li>No new software is needed for your vendors</li><li>Spend more time managing important materials</li></ul>
    </div>
    <div class="product" style="left:356px">
      <svg class="product__icon" viewBox="0 0 58 58"><ellipse cx="29" cy="18" rx="11" ry="4" fill="#6b449b"/><path d="M18 18 V40 A11 4 0 0 0 40 40 V18" fill="none" stroke="#6b449b" stroke-width="2.5"/><path d="M18 26 A11 4 0 0 0 40 26 M18 33 A11 4 0 0 0 40 33" fill="none" stroke="#6b449b" stroke-width="2.5"/></svg>
      <p class="product__title">Rapid Invoice</p>
      <ul class="product__list"><li>Receive your invoices and Invoice Images daily</li><li>Automatically matches invoice lines to PO lines</li><li>Imports Invoice Images into your Imaging system</li><li>Integrates with your Accounting system</li></ul>
    </div>
  </div>

  <div class="cta">
    <p class="cta__line">Let us show you how you can take your PO's to the next level</p>
    <div class="cta__pill">Call Crestline Supply on
      <svg viewBox="0 0 12 12"><circle cx="6" cy="6" r="5.2" fill="none" stroke="#fff" stroke-width="1"/><path d="M4 3.5 L5 5 L4.6 5.6 Q5.3 7 6.4 7.4 L7 7 L8.5 8 L7.8 8.9 Q5 8.6 3.2 4.3 Z" fill="#fff"/></svg>
      (800) 555-0142 &nbsp;for an obligation free quote</div>
  </div>
  <div class="footer">www.crsupsw.com</div>
</section>

</body>
</html>
```